Update Financial Planning Presentation

We currently use a stock Powerpoint template. Information is imputed into an Excel spreadsheet and then linked to the presentation. We are looking to improve and upgrade this to a more straightforward and "cleaner" looking template. I have attached a sample copy of the Powerpoint presantation we currently use along with the Excel spreadsheet. I have attached our logo as well. Thanks.
Industry/Entity Type
Financial

```html
<!DOCTYPE html>
<html lang="en">
<head>
<meta charset="utf-8">
<title>Larchway Financial – Planning Presentation</title>
<link href="https://fonts.googleapis.com/css2?family=Cormorant+Garamond:ital,wght@1,300&family=Quattrocento:wght@400;700&display=swap" rel="stylesheet">
<style>
:root{
  --stage:#5d5d5f;
  --paper:#ffffff;
  --green:#5fa35a;
  --green-dark:#2f8a3c;
  --ink:#111111;
  --text:#3c3c3c;
  --tree-light:#b9cf8c;
  --tree-dark:#6f8f3c;
}
*{box-sizing:border-box;margin:0;padding:0}
html,body{width:1200px;height:924px;overflow:hidden;background:var(--stage)}
body{position:relative;font-family:"Quattrocento",Georgia,serif;color:var(--text)}
.slide{position:absolute;width:497px;height:374px;background:var(--paper);box-shadow:7px 7px 9px rgba(0,0,0,.55);overflow:hidden}
.slide--lifecycle{left:78px;top:67px}
.slide--process{left:620px;top:65px}
.slide--personal{left:78px;top:488px}
.slide--expectancy{left:620px;top:488px}
.slide-number{position:absolute;left:453px;top:7px;width:22px;height:28px;background:var(--ink);color:#fff;font-size:11px;display:flex;align-items:center;justify-content:center}
.brand{position:absolute;left:10px;top:40px;display:flex;align-items:center;gap:4px;font-size:11px;font-weight:700;color:var(--green-dark)}
.brand-dot{width:6px;height:6px;background:var(--ink);border-radius:50%}
.slide-title{position:absolute;left:0;right:0;top:58px;text-align:center;font-family:"Cormorant Garamond",Georgia,serif;font-style:italic;font-weight:300;font-size:21px;color:#333}
.footer-band{position:absolute;left:0;right:0;bottom:0;height:15px;background:var(--green)}
.tree{position:absolute;left:410px;top:270px;width:82px;height:88px;border-radius:50% 50% 20% 20%;background:radial-gradient(circle at 50% 38%,var(--tree-light),var(--tree-dark) 75%,transparent 76%)}

/* lifecycle table */
.lifecycle-table{position:absolute;left:88px;top:99px;border-collapse:collapse;font-size:11px;color:#222}
.lifecycle-table th,.lifecycle-table td{border:1px solid #222;text-align:center;line-height:1.05}
.lifecycle-table th{font-weight:700;height:47px}
.lifecycle-table td{height:25px}
.lifecycle-table tr.tall td{height:32px}

/* process */
.process-steps{position:absolute;left:0;top:0}
.process-list{list-style:none;position:absolute;left:150px;top:0;font-size:11.5px;color:#444}
.process-list li{position:absolute;left:0;white-space:nowrap;transform:translateY(-50%)}

/* personal info form */
.form-head{position:absolute;top:93px;font-size:8px;font-weight:700;color:var(--green-dark)}
.client-form{position:absolute;left:62px;top:102px;width:332px;height:246px;border:1px solid #555}
.client-grid{border-collapse:collapse;width:100%;font-size:6.6px;table-layout:fixed}
.client-grid td{height:11px;text-align:center;padding:0;line-height:11px}
.client-grid .lbl{background:var(--green-dark);color:#e8f2e6;font-style:italic}
.client-grid .lbl-dark{background:var(--ink);color:#ddd;font-style:italic}
.client-grid .val{color:var(--green-dark);font-weight:700}
.address-grid{border-collapse:collapse;width:100%;font-size:6.6px;margin-top:1px;border-top:1px solid #999}
.address-grid td{height:17px;padding-left:12px;color:var(--green-dark)}
.address-grid .lbl-soft{color:#8bbf85;font-style:italic}
.children-bar{display:grid;grid-template-columns:48px 62px 48px 62px 46px 66px;background:var(--green-dark);color:#fff;font-size:6.6px;font-weight:700;height:8px;line-height:8px;text-align:center;margin-top:2px}
.children-list{list-style:none;font-size:6.6px;color:#8bbf85;font-style:italic}
.children-list li{height:17px;line-height:14px;padding-left:12px;display:grid;grid-template-columns:60px 40px}
.children-list span{color:var(--green-dark);font-style:normal}

/* expectancy */
.stat-card{position:absolute;top:106px;width:113px;height:179px;border-radius:14px;background:var(--green);color:#fff;text-align:center}
.stat-card--dark{background:var(--ink)}
.stat-badge{width:70px;height:70px;border-radius:50%;background:#fff;color:var(--ink);margin:16px auto 0;display:flex;align-items:center;justify-content:center;font-weight:700;font-size:12px;line-height:1.1}
.stat-list{list-style:none;font-size:10.5px;margin-top:0}
.stat-list li{height:30px;line-height:30px}
.chevron{position:absolute;top:226px}
</style>
</head>
<body>

<section class="slide slide--lifecycle">
  <div class="slide-number">1</div>
  <div class="brand"><span class="brand-dot"></span>Larchway Financial</div>
  <h1 class="slide-title">Common Lifecycle Periods</h1>
  <table class="lifecycle-table">
    <colgroup><col style="width:136px"><col style="width:65px"><col style="width:131px"></colgroup>
    <tr><th>Lifecycle<br>Periods</th><th>Age</th><th>Financial<br>Profile</th></tr>
    <tr><td>Early Career</td><td>25 – 40</td><td>Debts: Mortgage, etc.</td></tr>
    <tr><td>Mid-career</td><td>40 – 50</td><td>Debt Elimination</td></tr>
    <tr><td>Accumulation</td><td>50 – 60</td><td>Peak Savings Period</td></tr>
    <tr class="tall"><td>Pre-retirement</td><td>60- 65</td><td>Retirement &amp; Estate Planning</td></tr>
    <tr class="tall"><td>Retirement</td><td>Age 65+</td><td>Health and Lifestyle Changes</td></tr>
  </table>
  <div class="tree" role="img" aria-label="Leafy green tree illustration"></div>
  <div class="footer-band"></div>
</section>

<section class="slide slide--process">
  <div class="slide-number">2</div>
  <div class="brand"><span class="brand-dot"></span>Larchway Financial</div>
  <h1 class="slide-title">Financial Planning Process</h1>
  <svg class="process-steps" width="160" height="330" viewBox="0 0 160 330" font-family="Quattrocento, serif" font-size="11" text-anchor="middle">
    <g stroke="#3a6fb0" stroke-width="1">
      <circle cx="109" cy="303" r="21" fill="#111"/>
      <circle cx="77" cy="268" r="21" fill="#5fa35a" stroke="none"/>
      <circle cx="62" cy="227" r="21" fill="#111"/>
      <circle cx="63" cy="180" r="21" fill="#5fa35a" stroke="none"/>
      <circle cx="80" cy="138" r="21" fill="#111"/>
      <circle cx="106" cy="102" r="21" fill="#5fa35a" stroke="none"/>
    </g>
    <g fill="#fff">
      <text x="106" y="106">1</text><text x="80" y="142">2</text><text x="63" y="184">3</text>
      <text x="62" y="231">4</text><text x="77" y="272">5</text><text x="109" y="307">6</text>
    </g>
  </svg>
  <ol class="process-list">
    <li style="top:105px">Clarify Your present situation</li>
    <li style="top:142px">Identify Financial &amp; Personal Goals</li>
    <li style="top:180px">Identify Financial problems</li>
    <li style="top:220px">Create a Written Plan &amp; Strategies</li>
    <li style="top:261px">Implement Strategies &amp; Solutions</li>
    <li style="top:308px;left:4px">Ongoing Review &amp; Revision</li>
  </ol>
  <div class="tree" role="img" aria-label="Leafy green tree illustration"></div>
  <div class="footer-band"></div>
</section>

<section class="slide slide--personal">
  <div class="slide-number">3</div>
  <div class="brand"><span class="brand-dot"></span>Larchway Financial</div>
  <h1 class="slide-title">Personal Information</h1>
  <span class="form-head" style="left:106px">Client</span>
  <span class="form-head" style="left:346px">Contacts</span>
  <div class="client-form">
    <table class="client-grid">
      <colgroup><col style="width:47px"><col style="width:63px"><col style="width:47px"><col style="width:63px"><col style="width:45px"><col></colgroup>
      <tr><td class="lbl">Title</td><td class="val">Mr.</td><td class="lbl-dark">Title</td><td class="val">Mrs.</td><td class="lbl">Home #</td><td class="val">(604) 555 0142</td></tr>
      <tr><td class="lbl">First</td><td class="val">John</td><td class="lbl-dark">First</td><td class="val">Jane</td><td class="lbl">Work #</td><td></td></tr>
      <tr><td class="lbl">Initial</td><td></td><td class="lbl-dark">Initial</td><td></td><td class="lbl">Sp_Work #</td><td></td></tr>
      <tr><td class="lbl">Last</td><td class="val">Doe</td><td class="lbl-dark">Last</td><td class="val">Doe</td><td class="lbl">Fax #</td><td></td></tr>
      <tr><td class="lbl">DOB</td><td class="val">15 May 59</td><td class="lbl-dark">DOB</td><td class="val">5 Oct 58</td><td class="lbl">Mobile #</td><td></td></tr>
      <tr><td class="lbl">SIN</td><td class="val">123 456 789</td><td class="lbl-dark">SIN</td><td class="val">123 456 789</td><td class="lbl">Email #1</td><td></td></tr>
      <tr><td class="lbl">Age</td><td class="val">55.39</td><td class="lbl-dark">Age</td><td class="val">56.00</td><td class="lbl">Email #2</td><td></td></tr>
      <tr><td class="lbl">Age Change</td><td class="val">Nov 13</td><td class="lbl-dark">Age Change</td><td class="val">Apr 05</td><td class="lbl"></td><td></td></tr>
      <tr><td class="lbl">Smoker</td><td class="val">No</td><td class="lbl-dark">Smoker</td><td class="val">No</td><td class="lbl"></td><td></td></tr>
      <tr><td class="lbl">Occupation</td><td></td><td class="lbl-dark">Occupation</td><td></td><td class="lbl"></td><td></td></tr>
      <tr><td class="lbl">Status</td><td class="val">Married</td><td class="lbl-dark">Status</td><td class="val">Married</td><td class="lbl"></td><td></td></tr>
      <tr><td class="lbl">Health</td><td class="val">Excellent</td><td class="lbl-dark">Health</td><td class="val">Excellent</td><td class="lbl"></td><td></td></tr>
    </table>
    <table class="address-grid">
      <tr><td class="lbl-soft">Address</td><td><b>123 Street Name</b></td><td class="lbl-soft">City/Town</td><td></td><td class="lbl-soft">Province</td><td><b>BC</b></td></tr>
      <tr><td class="lbl-soft">Postal Code</td><td><b>V5N 2K7</b></td><td class="lbl-soft">Suite</td><td></td><td class="lbl-soft">Country</td><td><b>Canada</b></td></tr>
    </table>
    <div class="children-bar"><span>Children</span><span>Name</span><span></span><span></span><span>Age</span><span>Single/Married</span></div>
    <ul class="children-list">
      <li>Child 1<span>?</span></li>
      <li>Child 2<span>?</span></li>
      <li>Child 3<span>?</span></li>
      <li>Child 4<span></span></li>
    </ul>
  </div>
  <div class="tree" role="img" aria-label="Leafy green tree illustration"></div>
  <div class="footer-band"></div>
</section>

<section class="slide slide--expectancy">
  <div class="slide-number">8</div>
  <div class="brand"><span class="brand-dot"></span>Larchway Financial</div>
  <h1 class="slide-title">Life Expectancy</h1>
  <div class="stat-card" style="left:57px">
    <div class="stat-badge">Age</div>
    <ul class="stat-list"><li>•Age 65</li><li>•Age 75</li><li>•Age 85</li></ul>
  </div>
  <svg class="chevron" style="left:171px" width="12" height="18" viewBox="0 0 12 18"><path d="M0 0h5l7 9-7 9H0l7-9z" fill="#111"/></svg>
  <div class="stat-card stat-card--dark" style="left:183px">
    <div class="stat-badge">Male Life<br>Expectancy</div>
    <ul class="stat-list"><li>•19.20 Years</li><li>•11.15 Years</li><li>• 6.35 Years</li></ul>
  </div>
  <svg class="chevron" style="left:297px" width="12" height="18" viewBox="0 0 12 18"><path d="M0 0h5l7 9-7 9H0l7-9z" fill="#111"/></svg>
  <div class="stat-card" style="left:309px">
    <div class="stat-badge">Female Life<br>Expectancy</div>
    <ul class="stat-list"><li>•22.00 Years</li><li>•13.54 Years</li><li>• 7.49 Years</li></ul>
  </div>
  <div class="tree" role="img" aria-label="Leafy green tree illustration"></div>
  <div class="footer-band"></div>
</section>

</body>
</html>
```